Strata Edge Supply Business Card Design Challenge

Please create me a simple card using my logo. I'm not looking for anything abstract.
A couple of colours for text and maybe something on the card so the whole card isn't just a white board.
Please send me samples and I'll reply with suggestions to refine the design. Thank you

Reason: The Ormeau address was incorrect in the brief, so I have updated that so the 4 and 5 star submissions can be updated and resubmitted please!!! Sorry and thank you

Target Market(s)

Mining companies and rock producing aggregate companies. Quarries

Industry/Entity Type

Mining

Contact Information for Business Card

Name - Lewis Trenholm / Company Logo AND Strata Edge Supply Pty Ltd / position - Managing Director / address1 - Unit 3, 14 Kestrel Parade, Calder Ridge 4281 Queensland AU / address2 - PO Box 917, Brayfield 4295 Queensland AU / mobile - 0427 195 864 / phone - 07 5571 9346 / fax - 07 5571 9420 / email - lt@strataedgesupply.example.com.au / website - www.strataedgesupply.example.com.au

Requirements
Must have
• Business details as per the above. The phone and fax numbers will be confirmed before the end of the project. Thank you
• SINGLE SIDED ONLY please on Card, not transparent plastic

```html
<!DOCTYPE html>
<html lang="en">
<head>
<meta charset="utf-8">
<title>Strata Edge Supply – Business Card</title>
<link href="https://fonts.googleapis.com/css2?family=Lato:wght@400;700;900&display=swap" rel="stylesheet">
<style>
  :root {
    --backdrop: #e9e9ea;
    --card: #ffffff;
    --brand-blue: #1ea6de;
    --brand-blue-deep: #1791c4;
    --ink-grey: #4a4b4d;
    --logo-grey: #58595b;
    --on-blue: #ffffff;
  }
  * { box-sizing: border-box; margin: 0; padding: 0; }
  html, body {
    width: 1200px; height: 600px; overflow: hidden;
    background: var(--backdrop);
    font-family: "Lato", Arial, sans-serif;
  }
  .canvas {
    width: 1200px; height: 600px;
    display: flex; align-items: center; justify-content: center;
  }
  .business-card {
    position: relative;
    width: 945px; height: 540px;
    background: var(--card);
    border-radius: 10px;
    overflow: hidden;
    box-shadow: 0 6px 24px rgba(0,0,0,0.12);
  }
  .brand {
    position: absolute; top: 62px; right: 64px;
    display: flex; align-items: center; gap: 16px;
  }
  .brand-mark {
    width: 46px; height: 46px;
    background: var(--brand-blue);
  }
  .brand-name {
    font-weight: 900; font-size: 38px;
    color: var(--logo-grey);
    letter-spacing: 0.5px;
  }
  .identity {
    position: absolute; left: 64px; top: 238px;
  }
  .person-name {
    font-weight: 900; font-size: 40px;
    color: var(--brand-blue);
    line-height: 1.1;
  }
  .person-title {
    font-size: 27px; color: var(--ink-grey);
    margin-top: 4px;
  }
  .contact-band {
    position: absolute; left: 0; right: 0; bottom: 0;
    height: 196px;
    background: var(--brand-blue);
    border-bottom: 10px solid var(--brand-blue-deep);
    display: flex; justify-content: space-between;
    padding: 24px 60px 0 64px;
    color: var(--on-blue);
  }
  .contact-list { list-style: none; }
  .contact-list li {
    display: flex; align-items: center; gap: 12px;
    font-size: 22px; line-height: 30px;
  }
  .contact-list svg { width: 20px; height: 20px; flex: none; }
  .address-block {
    text-align: right;
    font-style: normal;
    font-size: 22px; line-height: 32px;
    padding-top: 6px;
  }
</style>
</head>
<body>
<div class="canvas">
  <article class="business-card">
    <header class="brand">
      <span class="brand-mark"></span>
      <span class="brand-name">Strata Edge Supply</span>
    </header>

    <section class="identity">
      <h1 class="person-name">Lewis Trenholm</h1>
      <p class="person-title">Managing Director</p>
    </section>

    <footer class="contact-band">
      <ul class="contact-list">
        <li>
          <svg viewBox="0 0 20 20" aria-hidden="true"><rect x="5" y="1" width="10" height="18" rx="2" fill="none" stroke="currentColor" stroke-width="2"/><circle cx="10" cy="15.5" r="1.2" fill="currentColor"/></svg>
          0427 195 864
        </li>
        <li>
          <svg viewBox="0 0 20 20" aria-hidden="true"><path d="M2 8c0-3 4-4 8-4s8 1 8 4v2h-4V8H6v2H2z" fill="currentColor"/><rect x="4" y="11" width="12" height="7" rx="1" fill="currentColor"/></svg>
          07 5571 9346
        </li>
        <li>
          <svg viewBox="0 0 20 20" aria-hidden="true"><rect x="5" y="2" width="10" height="6" fill="none" stroke="currentColor" stroke-width="2"/><rect x="2" y="8" width="16" height="8" rx="1" fill="currentColor"/><rect x="5" y="14" width="10" height="4" fill="currentColor"/></svg>
          07 5571 9420
        </li>
        <li>
          <svg viewBox="0 0 20 20" aria-hidden="true"><rect x="1" y="4" width="18" height="12" rx="1" fill="currentColor"/><path d="M1.5 4.5 10 11l8.5-6.5" fill="none" stroke="#1ea6de" stroke-width="1.6"/></svg>
          lt@strataedgesupply.example.com.au
        </li>
        <li>
          <svg viewBox="0 0 20 20" aria-hidden="true"><circle cx="10" cy="10" r="8.5" fill="none" stroke="currentColor" stroke-width="1.8"/><ellipse cx="10" cy="10" rx="3.5" ry="8.5" fill="none" stroke="currentColor" stroke-width="1.5"/><path d="M1.5 10h17M3 5.5h14M3 14.5h14" stroke="currentColor" stroke-width="1.3"/></svg>
          www.strataedgesupply.example.com.au
        </li>
      </ul>
      <address class="address-block">
        Address1 - Unit 3, 14 Kestrel Parade<br>
        Calder Ridge 4281 Queensland AU<br>
        Address2 - PO Box 917<br>
        Brayfield 4295 Queensland AU
      </address>
    </footer>
  </article>
</div>
</body>
</html>
```